Construction company focused on concrete and shed construction.

We need to update our current business card for ridgeforgebuilds.com.au we would like an eye catching design with blue, grey and white incorporating our current logo.
Our company started off in concreting and due to varying factors we have expanded to include shed construction as well.
This has led to our current Logo looking a little out of place and somehow need to use the card to bring in the shed construction side of the business while not having to change current concrete look "KESTRO" logo as we already have this incorporated into our company clothing and are not willing to change this yet.
Photo image attached for inspiration/ visual reference of type of work, not to be used on final design.
Please no cheesy designs of men in hard hats and tools
Final design should demonstrate a modern and service focused company.

Target Market(s)

Farmers, Business owners, Developers, Architects, Commercial project delivery

Industry/Entity Type

Construction Company

Contact Information for Business Card

Kestro Constructions.
7b Harlow st
East Corvale Vic
03 62918873

Font styles to use
Other font styles liked:
• see font in logo

Colors
3176b5
b2b2b2

Requirements
Must have
• Easy to read font,
• good contrast between back ground and writing
Nice to have
• Modern and corporate look with a fun but professional image.
Should not have
• Comic images or shadow images of tools/ people.

```html
<!DOCTYPE html>
<html lang="en">
<head>
<meta charset="utf-8">
<title>Kestro Group – Business Card</title>
<link href="https://fonts.googleapis.com/css2?family=Roboto:wght@400;500&family=Roboto+Condensed:wght@700&display=swap" rel="stylesheet">
<style>
  :root {
    --backdrop: #2b2b2b;
    --card: #f4f4f3;
    --brand-blue: #1f5f9a;
    --accent-blue: #3176b5;
    --grey: #b2b2b2;
    --ink: #4a4a4a;
    --ink-soft: #555555;
  }
  * { margin: 0; padding: 0; box-sizing: border-box; }
  html, body { width: 1200px; height: 960px; overflow: hidden; }
  body {
    background: var(--backdrop);
    position: relative;
    font-family: "Roboto", Arial, sans-serif;
  }
  .card {
    position: absolute;
    width: 600px;
    height: 342px;
    background: var(--card);
    border-radius: 20px;
    overflow: hidden;
  }
  .card--front { left: 314px; top: 113px; }
  .card--back  { left: 311px; top: 472px; }

  .wordmark {
    position: absolute;
    font-family: "Roboto Condensed", "Arial Narrow", sans-serif;
    font-weight: 700;
    color: var(--brand-blue);
    border-top: 1px solid var(--grey);
    border-bottom: 1px solid var(--grey);
    white-space: nowrap;
  }
  .brand-circle { position: absolute; }

  /* front */
  .card--front .brand-circle { left: 268px; top: 50px; }
  .card--front .wordmark {
    left: 372px; top: 76px; width: 191px;
    font-size: 26px; line-height: 30px; letter-spacing: 0.8px; text-align: center;
  }
  .person { position: absolute; left: 36px; top: 197px; }
  .person__name {
    font-family: "Roboto Condensed", "Arial Narrow", sans-serif;
    font-weight: 700; font-size: 21px; line-height: 24px;
    color: var(--brand-blue);
  }
  .person__role {
    font-size: 14.5px; font-weight: 500; color: var(--ink-soft);
    line-height: 18px;
  }
  .contact-list {
    position: absolute; left: 36px; top: 252px; list-style: none;
  }
  .contact-list li {
    display: flex; align-items: center; gap: 8px;
    font-size: 14.5px; color: var(--ink); height: 19px;
  }
  .contact-list svg { width: 14px; height: 14px; fill: var(--brand-blue); }
  .divider {
    position: absolute; left: 308px; top: 260px;
    width: 1px; height: 48px; background: var(--ink);
  }
  .address {
    position: absolute; left: 325px; top: 258px;
    font-size: 14.5px; line-height: 19px; color: var(--ink);
    font-style: normal;
  }

  /* back */
  .card--back .brand-circle { left: 314px; top: 48px; }
  .card--back .wordmark {
    left: 35px; top: 252px; width: 249px;
    font-size: 33px; line-height: 40px; letter-spacing: 2.6px;
  }
  .web {
    position: absolute; left: 35px; top: 296px;
    font-size: 14.5px; letter-spacing: 1.2px; color: var(--ink);
  }
</style>
</head>
<body>

<section class="card card--front">
  <svg class="brand-circle" width="90" height="90" viewBox="0 0 90 90" aria-hidden="true">
    <circle cx="45" cy="45" r="40" fill="none" stroke="var(--accent-blue)" stroke-width="4"/>
  </svg>
  <div class="wordmark">KESTRO GROUP</div>

  <div class="person">
    <div class="person__name">LIAM CARVER</div>
    <div class="person__role">CEO/FOUNDER</div>
  </div>

  <ul class="contact-list">
    <li>
      <svg viewBox="0 0 24 24"><path d="M6.6 10.8a15.1 15.1 0 0 0 6.6 6.6l2.2-2.2c.3-.3.7-.4 1-.2 1.1.4 2.3.6 3.6.6.6 0 1 .4 1 1V20c0 .6-.4 1-1 1C10.6 21 3 13.4 3 4c0-.6.4-1 1-1h3.5c.6 0 1 .4 1 1 0 1.3.2 2.5.6 3.6.1.3 0 .7-.2 1z"/></svg>
      03 62918873
    </li>
    <li>
      <svg viewBox="0 0 24 24"><path d="M2 5h20v2l-10 6L2 7z"/><path d="M2 9l10 6 10-6v10H2z"/></svg>
      info@ridgeforgebuilds.com.au
    </li>
    <li>
      <svg viewBox="0 0 24 24"><circle cx="12" cy="12" r="10"/><path d="M8 6c2 1 1 3 3 4s1 3 0 4-1 3 0 5M15 4c-1 2 1 3 3 3M17 14c-2 0-3 2-2 4" stroke="var(--card)" stroke-width="1.6" fill="none"/></svg>
      ridgeforgebuilds.com.au
    </li>
  </ul>

  <div class="divider"></div>
  <address class="address">
    Kestro Constructions<br>
    7b Harlow st<br>
    East Corvale Vic
  </address>
</section>

<section class="card card--back">
  <svg class="brand-circle" width="240" height="240" viewBox="0 0 240 240" aria-hidden="true">
    <circle cx="120" cy="120" r="112" fill="#e3e5e8" stroke="var(--accent-blue)" stroke-width="5"/>
  </svg>
  <div class="wordmark">KESTRO GROUP</div>
  <div class="web">www.ridgeforgebuilds.com.au</div>
</section>

</body>
</html>
```